Create Vertical Dog Food Labels (3 inches x 5 inches) for Pawlyn Kitchen

We need a packing Vertical label (3 inches x 5 inches) design for our line of Dog Food - Pawlyn Kitchen at pawlynkitchen.com (please review website). This design is for Custom Roll Labels. We have a logo already. Use our logo colors on label. What we need incorporated is a list of our ingredients:

50% Choice Beef
20% Pasture-raised Chicken
15% Brown Rice
15% Fresh Vegetables - Carrots, Kale, Zucchini
Herbal Health Boosters

We also need these lines at the bottom of the label:

Keeps in fridge for 4 days after thawing
Stores in freezer up to 6 months
Questions? email us at orders@brindlecopsepantry.com

We have attached a sample of a competitor. The Meadow Bowl.

Target Market(s)

Dog owners

Industry/Entity Type

Dog Food

Font styles to use
Sans Serif

Requirements
Must have
• Read project description above
Nice to have
• Our logo color incorporated
Should not have
• I want it simple.

```html
<!DOCTYPE html>
<html lang="en">
<head>
<meta charset="utf-8">
<title>Pawlyn Kitchen – Dog Food Label</title>
<link rel="stylesheet" href="https://fonts.googleapis.com/css2?family=Outfit:wght@300;400;600;700&display=swap">
<style>
  :root {
    --backdrop: #48271d;
    --label-white: #ffffff;
    --ink: #111111;
    --brand-green: #14703c;
    --dog-brown: #4a2219;
  }
  * { margin: 0; padding: 0; box-sizing: border-box; }
  html, body { width: 1200px; height: 1200px; overflow: hidden; }
  body {
    background: var(--backdrop);
    font-family: "Outfit", sans-serif;
    color: var(--ink);
    position: relative;
  }
  .label-frame { position: absolute; left: 0; top: 0; width: 1200px; height: 1200px; }
  .brand {
    position: absolute; left: 470px; top: 272px;
    display: flex; align-items: center; gap: 14px;
  }
  .brand-dot { width: 72px; height: 72px; border-radius: 50%; background: var(--brand-green); }
  .brand-name { font-size: 30px; font-weight: 600; color: var(--brand-green); letter-spacing: 0.5px; }
  .section-title {
    position: absolute; left: 425px; width: 356px; top: 348px;
    text-align: center; font-size: 25px; font-weight: 700; letter-spacing: 0.3px;
  }
  .rule { position: absolute; left: 425px; width: 356px; height: 1px; background: var(--ink); }
  .rule.top { top: 388px; }
  .rule.bottom { top: 605px; }
  .ingredients {
    position: absolute; left: 396px; width: 414px; top: 402px;
    list-style: none; text-align: center; font-weight: 300;
  }
  .ingredients li { font-size: 25px; line-height: 32px; }
  .ingredients .sub { font-size: 22px; line-height: 28px; margin-top: -2px; }
  .ingredients .boost { font-size: 18px; font-weight: 700; line-height: 34px; }
  .illustration {
    position: absolute; left: 515px; top: 621px; width: 250px; height: 146px;
    background: linear-gradient(90deg, var(--dog-brown) 0%, var(--dog-brown) 60%, #f2ecea 100%);
    border-radius: 40px 60px 8px 8px;
  }
  .storage-band {
    position: absolute; left: 396px; top: 767px; width: 414px; height: 56px;
    background: var(--brand-green); color: var(--label-white);
    font-size: 17px; font-weight: 600; line-height: 21px;
    padding: 7px 0 0 14px;
  }
  .storage-band span { display: block; }
  .storage-band span + span { padding-left: 20px; }
  .contact-email {
    position: absolute; left: 396px; width: 414px; top: 829px;
    text-align: center; font-size: 20px; font-weight: 300;
  }
  .web-pill {
    position: absolute; left: 396px; top: 877px; width: 408px; height: 34px;
    border-radius: 17px; background: var(--brand-green); color: var(--label-white);
    text-align: center; font-size: 21px; font-weight: 300; line-height: 34px;
  }
</style>
</head>
<body>
  <svg class="label-frame" viewBox="0 0 1200 1200" aria-hidden="true">
    <path fill="#ffffff" d="M373 262 C373 245 385 236 398 231 C414 224 420 212 422 193 L470 193 C482 193 486 200 490 203 C520 165 560 144 597 144 C636 144 676 165 706 203 C710 200 714 193 726 193 L784 193 C786 212 792 224 808 231 C822 236 834 245 834 262 L834 915 C834 930 822 941 808 941 L398 941 C385 941 373 930 373 915 Z"/>
    <path fill="none" stroke="#111" stroke-width="4.5" d="M382 270 C382 255 392 248 404 243 C420 237 428 226 430 208 L478 208 C486 208 488 212 492 216 C524 178 560 159 597 159 C634 159 670 178 702 216 C706 212 708 208 716 208 L776 208 C778 226 786 237 802 243 C814 248 824 255 824 270 L824 910 C824 919 818 925 809 925 L397 925 C388 925 382 919 382 910 Z"/>
    <path fill="none" stroke="#111" stroke-width="1.6" d="M396 280 C396 266 404 260 414 256 C430 250 438 238 442 221 L478 221 C484 221 486 230 490 232 C494 233 496 230 498 228 C526 193 560 175 598 175 C636 175 670 193 698 228 C700 230 702 233 706 232 C710 230 712 221 718 221 L762 221 C766 238 774 250 790 256 C800 260 810 266 810 280 L810 855 C810 860 806 863 801 863 L405 863 C400 863 396 860 396 855 Z"/>
  </svg>

  <div class="brand">
    <span class="brand-dot"></span>
    <span class="brand-name">Pawlyn Kitchen</span>
  </div>

  <h2 class="section-title">INGREDIENTS</h2>
  <div class="rule top"></div>
  <ul class="ingredients">
    <li>50% Choice Beef</li>
    <li>20% Pasture-raised Chicken</li>
    <li>15% Brown Rice</li>
    <li>15% Fresh Vegetables -</li>
    <li class="sub">Carrots, Kale, Zucchini</li>
    <li class="boost">HERBAL HEALTH BOOSTERS</li>
  </ul>
  <div class="rule bottom"></div>

  <div class="illustration" role="img" aria-label="Brown silhouette of a sitting dog with a speech bubble reading Dog Food"></div>

  <div class="storage-band">
    <span>KEEPS IN FRIDGE FOR 4 DAYS AFTER THAWING</span>
    <span>STORES IN FREEZER UP TO 6 MONTHS</span>
  </div>
  <p class="contact-email">orders@brindlecopsepantry.com</p>
  <div class="web-pill">pawlynkitchen.com</div>
</body>
</html>
```